Bourbon label design for bourbon brand. Looking to freshen our current label.

I need a Bourbon label design for our rebranded Bourbon bottle. Label should include picture of our horse and our logo on the bottle. Front Label is 3.5 inches wide and 6 inches tall, back label is 4 inches tall and 3 inches wide. Back label can be a simple plain logo like the one in the brief. I have included a design of our current bottle and label. We want to stay close to the current color schemes but want a fresh rebrand of the design. The label needs to be the correct size on a tall bottle like pictured.

Target Market(s)

Our Bourbon members, 30-50 year old males

Requirements
Must have
• Picture of our horse, our B logo , straight Bourbon whiskey on the front. Room to edit text on the back label.

```html
<!DOCTYPE html>
<html lang="en">
<head>
<meta charset="utf-8">
<title>Nightfall Straight Bourbon Whiskey – Front Label</title>
<link rel="stylesheet" href="https://fonts.googleapis.com/css2?family=Playfair+Display+SC:wght@700&family=Roboto+Slab:wght@500;700&family=Pinyon+Script&display=swap">
<style>
  :root {
    --backdrop: #2f2f31;
    --label-black: #131313;
    --gold: #b8996c;
    --gold-soft: #8a7352;
    --cream: #e6dcc6;
    --title-white: #f3f1ec;
    --photo-dark: #2a2a2a;
    --photo-light: #9a9a9a;
  }
  html, body {
    margin: 0;
    padding: 0;
    width: 834px;
    height: 1200px;
    overflow: hidden;
    background: var(--backdrop);
  }
  .label-art {
    display: block;
    width: 834px;
    height: 1200px;
  }
  .label-band { fill: var(--label-black); }
  .frame-line { fill: none; stroke: var(--gold); stroke-width: 2; }
  .frame-line-thin { fill: none; stroke: var(--gold-soft); stroke-width: 1.2; }
  .brand-title {
    font-family: "Playfair Display SC", Georgia, serif;
    font-weight: 700;
    fill: var(--title-white);
  }
  .slab-text {
    font-family: "Roboto Slab", Georgia, serif;
    font-weight: 700;
    fill: var(--cream);
  }
  .slab-small {
    font-family: "Roboto Slab", Georgia, serif;
    font-weight: 500;
    fill: var(--cream);
    letter-spacing: 1px;
  }
  .gold-text { fill: var(--gold); }
  .script-text {
    font-family: "Pinyon Script", cursive;
    fill: var(--title-white);
  }
  .horse-photo { fill: url(#photoTone); }
  .brand-seal { fill: none; stroke: var(--gold); stroke-width: 2; }
</style>
</head>
<body>
<svg class="label-art" viewBox="0 0 834 1200" xmlns="http://www.w3.org/2000/svg">
  <defs>
    <linearGradient id="photoTone" x1="0" y1="0" x2="1" y2="1">
      <stop offset="0" stop-color="var(--photo-light)"/>
      <stop offset="0.55" stop-color="#5a5a5a"/>
      <stop offset="1" stop-color="var(--photo-dark)"/>
    </linearGradient>
  </defs>

  <!-- label band -->
  <rect class="label-band" x="25" y="274" width="785" height="788"/>

  <!-- upper pediment frame -->
  <g class="upper-frame">
    <path class="frame-line" d="M150 405 L150 488 L285 488 L285 450 Z"/>
    <path class="frame-line" d="M680 405 L680 488 L545 488 L545 450 Z"/>
    <path class="frame-line-thin" d="M90 482 L90 420 L290 455"/>
    <path class="frame-line-thin" d="M750 482 L750 420 L540 455"/>
    <circle class="frame-line-thin" cx="417" cy="470" r="115"/>
  </g>

  <!-- main panel frame -->
  <rect class="frame-line" x="90" y="482" width="660" height="435"/>
  <rect class="frame-line-thin" x="100" y="492" width="640" height="415"/>
  <path class="frame-line-thin" d="M180 760 L180 705 L655 705 L655 760"/>
  <path class="frame-line-thin" d="M130 905 L130 870 L320 870"/>
  <path class="frame-line-thin" d="M710 905 L710 870 L515 870"/>

  <!-- horse photograph -->
  <path class="horse-photo" role="img" aria-label="Photograph of the brand's racehorse galloping with jockey"
        d="M330 212 Q360 170 420 172 Q490 178 510 250 Q530 330 515 410 Q505 480 470 540 Q450 600 400 610 Q360 600 355 540 Q320 470 318 380 Q310 280 330 212 Z"/>

  <!-- established -->
  <text class="slab-text" x="218" y="477" font-size="38" text-anchor="middle">EST</text>
  <text class="slab-text" x="612" y="477" font-size="38" text-anchor="middle">2016</text>

  <!-- brand name -->
  <text class="brand-title" x="417" y="688" font-size="140" text-anchor="middle" textLength="545" lengthAdjust="spacingAndGlyphs">Nightfall</text>

  <!-- product -->
  <text class="slab-text" x="417" y="742" font-size="33" text-anchor="middle" textLength="410" lengthAdjust="spacingAndGlyphs">STRAIGHT BOURBON</text>
  <text class="script-text" x="417" y="820" font-size="78" text-anchor="middle">Whiskey</text>

  <!-- barrel details -->
  <text class="slab-small" x="160" y="789" font-size="13" text-anchor="middle">BARREL NO.</text>
  <text class="slab-text" x="160" y="832" font-size="36" text-anchor="middle">28</text>
  <text class="slab-small" x="680" y="789" font-size="15" text-anchor="middle">ALC VOL.</text>
  <text class="slab-text gold-text" x="680" y="832" font-size="36" text-anchor="middle">66%</text>

  <!-- age box -->
  <rect class="frame-line" x="320" y="872" width="195" height="50" fill="var(--label-black)"/>
  <text class="slab-text" x="417" y="907" text-anchor="middle">
    <tspan font-size="20">AGE </tspan><tspan font-size="32">10</tspan><tspan font-size="20"> YRS</tspan>
  </text>

  <!-- lower pediment -->
  <g class="lower-frame">
    <path class="frame-line" d="M160 960 L160 1062 M160 960 L290 975 L290 1062"/>
    <path class="frame-line" d="M675 960 L675 1062 M675 960 L545 975 L545 1062"/>
    <path class="frame-line-thin" d="M100 940 L740 940"/>
  </g>
  <text class="slab-small" x="222" y="1000" font-size="17" text-anchor="middle">SINGLE</text>
  <text class="slab-small" x="222" y="1024" font-size="17" text-anchor="middle">BARREL</text>
  <text class="slab-small" x="614" y="1000" font-size="17" text-anchor="middle">BARREL</text>
  <text class="slab-small" x="614" y="1024" font-size="17" text-anchor="middle">STRENGTH</text>

  <!-- brand seal -->
  <circle class="brand-seal" cx="417" cy="1004" r="58"/>
  <text class="slab-text" x="417" y="1010" font-size="16" text-anchor="middle">NIGHTFALL</text>
</svg>
</body>
</html>
```